Cutting Edge Cloud Hosting Provider needs business card design

We are a new Cloud Hosting Provider called Verdalo Hosting. (Verdalo means cloudy in Spanish.) We provide clients with virtual resources and not virtual machines directly. Our clients purchase the resources that they will use (RAM,CPU, Hard drive space) then use those resources in as many virtual machines as they like.

We are looking for a business card design that is cutting edge and hip.
Updates

The name of the company is "Verdalo Hosting". Please include the "Hosting" part of our name in the design.

Thanks

Target Market(s)

21-35 developers and I.T. Staff

Industry/Entity Type

Business

Requirements
Must have
• Rounded corners, Must Incorporate our logo, individual's name must be prominent

```html
<!DOCTYPE html>
<html lang="en">
<head>
<meta charset="utf-8">
<title>Verdalo Hosting — Business Card</title>
<link href="https://fonts.googleapis.com/css2?family=Source+Sans+3:wght@400;600&display=swap" rel="stylesheet">
<style>
  :root {
    --page-light: #ffffff;
    --page-edge: #e6e6e6;
    --navy-deep: #0a1847;
    --navy: #10266a;
    --navy-glow: #1e4a9a;
    --card-white: #ffffff;
    --card-silver: #dedede;
    --ink-light: #ffffff;
    --ink-soft: #dfe6f5;
  }
  * { margin: 0; padding: 0; box-sizing: border-box; }
  html, body {
    width: 1200px;
    height: 900px;
    overflow: hidden;
  }
  body {
    position: relative;
    background: radial-gradient(ellipse at 50% 40%, var(--page-light) 0%, var(--page-light) 45%, var(--page-edge) 100%);
    font-family: "Source Sans 3", Arial, sans-serif;
  }
  .card {
    position: absolute;
    border-radius: 16px;
    overflow: hidden;
    box-shadow: 0 4px 10px rgba(0, 0, 0, 0.25);
  }
  .card-front {
    left: 57px;
    top: 333px;
    width: 518px;
    height: 297px;
    background: linear-gradient(90deg, var(--navy) 0%, var(--navy-deep) 100%);
  }
  .front-panel {
    position: absolute;
    inset: 0;
    width: 100%;
    height: 100%;
  }
  .front-wordmark {
    position: absolute;
    left: 36px;
    top: 104px;
    width: 190px;
    font-size: 44px;
    font-weight: 600;
    line-height: 44px;
    letter-spacing: 0.5px;
    color: var(--navy);
  }
  .holder-name {
    position: absolute;
    left: 298px;
    top: 52px;
    font-size: 34px;
    font-weight: 400;
    line-height: 1;
    color: var(--ink-light);
  }
  .contact-list {
    position: absolute;
    left: 356px;
    top: 180px;
    list-style: none;
    font-size: 15px;
    line-height: 20px;
    color: var(--ink-soft);
  }
  .card-back {
    left: 630px;
    top: 335px;
    width: 513px;
    height: 295px;
    background: radial-gradient(ellipse at 50% 45%, var(--navy-glow) 0%, var(--navy) 45%, var(--navy-deep) 100%);
    display: flex;
    align-items: center;
    justify-content: center;
  }
  .back-wordmark {
    font-size: 54px;
    font-weight: 600;
    line-height: 1;
    letter-spacing: 0.5px;
    white-space: nowrap;
    color: var(--ink-light);
    margin-top: -8px;
  }
</style>
</head>
<body>
  <section class="card card-front" aria-label="Business card front">
    <svg class="front-panel" viewBox="0 0 518 297" preserveAspectRatio="none" aria-hidden="true">
      <defs>
        <linearGradient id="silver" x1="0" y1="0" x2="0" y2="1">
          <stop offset="0" stop-color="var(--card-white)"/>
          <stop offset="0.55" stop-color="var(--card-white)"/>
          <stop offset="1" stop-color="var(--card-silver)"/>
        </linearGradient>
      </defs>
      <path d="M0 0 H153
               C205 0 246 30 243 68
               C241 86 233 98 230 106
               C285 110 322 150 318 208
               C315 250 305 280 303 297
               H0 Z"
            fill="url(#silver)"/>
    </svg>
    <div class="front-wordmark">Verdalo Hosting</div>
    <h1 class="holder-name">Marco Ellison</h1>
    <ul class="contact-list">
      <li>Vice-President</li>
      <li>p. 210.555.0142</li>
      <li>c. 210.555.0187</li>
      <li>marco@verdalo.com</li>
    </ul>
  </section>

  <section class="card card-back" aria-label="Business card back">
    <div class="back-wordmark">Verdalo Hosting</div>
  </section>
</body>
</html>
```